Say Something About Privacy!!!

We need a poster designed with the theme of "Privacy". With so many digital assistants (Vela, Moribel, Trunzo, etc) listening to our conversations and web cams watching our activities privacy is becoming more important than ever. The goal of the project is to design a poster that can be used as giveaway item at trade shows, etc. The poster should be engaging and thought provoking. The tone can be serious or lighthearted. You can use a photo, illustration, or just copy to get your point across. I've included a few examples of other posters I like.

Target Market(s)

General Public. Well educated. Tech enthusiasts. People with smartphones and/or smart speakers.

Industry/Entity Type

Cyber Security

Font styles to use
Sans Serif

Requirements
Must have
• Simple design. Strong colours.
Should not have
• While this is a serious subject, I don't want the message to be too threatening.

```html
<!DOCTYPE html>
<html lang="en">
<head>
<meta charset="utf-8">
<title>Privacy Posters</title>
<link href="https://fonts.googleapis.com/css2?family=Poppins:wght@700&family=Montserrat:wght@700&display=swap" rel="stylesheet">
<style>
  :root {
    --page: #f2f2f4;
    --navy: #2b2763;
    --paper: #e8e9eb;
    --ink: #111111;
    --stripe-mid: #7a7b7e;
    --light: #ececef;
    --sky: #1fa8e0;
    --alert: #ee3a2f;
  }
  html, body {
    margin: 0;
    padding: 0;
    width: 1200px;
    height: 857px;
    overflow: hidden;
    background: var(--page);
  }
  .canvas {
    position: relative;
    width: 1200px;
    height: 857px;
  }
  .poster {
    position: absolute;
    top: 110px;
    width: 440px;
    height: 622px;
  }
  .poster--think {
    left: 126px;
    background: var(--navy);
  }
  .poster--question {
    left: 625px;
    background: var(--paper);
  }
  .slogan {
    position: absolute;
    left: 0;
    top: 0;
    margin: 0;
    font-family: "Poppins", sans-serif;
    font-weight: 700;
    font-size: 87px;
    letter-spacing: -0.035em;
    line-height: 1;
  }
  .slogan__line {
    position: absolute;
    white-space: nowrap;
  }
  .slogan__line--think  { left: 62px;  top: 144px; color: var(--light); }
  .slogan__line--before { left: 113px; top: 221px; color: var(--light); }
  .slogan__line--you    { left: 60px;  top: 300px; color: var(--sky); }
  .slogan__line--agree  { left: 110px; top: 379px; color: var(--sky); }
  .headline {
    position: absolute;
    left: 82px;
    top: 97px;
    margin: 0;
    font-family: "Montserrat", sans-serif;
    font-weight: 700;
    font-size: 15px;
    letter-spacing: 0.18em;
    color: var(--ink);
    white-space: nowrap;
  }
  .headline__accent { color: var(--alert); }
  .striped-mark {
    position: absolute;
    left: 82px;
    top: 122px;
    width: 277px;
    height: 409px;
    background: linear-gradient(180deg, var(--stripe-mid) 0%, var(--ink) 100%);
  }
</style>
</head>
<body>
<main class="canvas">
  <section class="poster poster--think">
    <h1 class="slogan">
      <span class="slogan__line slogan__line--think">think</span>
      <span class="slogan__line slogan__line--before">before</span>
      <span class="slogan__line slogan__line--you">you</span>
      <span class="slogan__line slogan__line--agree">agree</span>
    </h1>
  </section>

  <section class="poster poster--question">
    <h2 class="headline">IS YOUR DATA <span class="headline__accent">SAFE</span> ONLINE</h2>
    <div class="striped-mark" role="img" aria-label="Large question mark formed by gaps in horizontal black stripes"></div>
  </section>
</main>
</body>
</html>
```